Design a New Site for a very cool Watch

We have the overall design element of the website and the banners in the PSD file. We need someone to finish our design in PSD and than convert to HTML. We have included the instructions, PSD file, images and all text.

We currently use Hubspot to host and make changes to our site. The entire design aspect is complete so all we need is some minor changes and additions within the photoshop design and than the coding into HTML.

Please only sign up if you understand photoshop and HTML conversion

Here is the DropBox link to the files
https://www.filemarrow.com/s/qk7vbn3lwpe9tdx/Velqor%20Site.zip
Updates

We have the basic design concept in Photoshop.  We just need someone who can complete some changes, make some additions and convert to HTML

Target Market(s)

Watch Buyers

Requirements
Must have
• Must look like a professional luxury brand

Our brand colors are very basic with Black, White and Grey can be used

```html
<!DOCTYPE html>
<html lang="en">
<head>
<meta charset="utf-8">
<title>Velqor &amp; Co.</title>
<link rel="stylesheet" href="https://fonts.googleapis.com/css2?family=Cinzel:wght@400&family=Montserrat:wght@300;400&display=swap">
<style>
:root{
  --white:#ffffff;
  --black:#000000;
  --ink:#222222;
  --band:#2e2e2e;
  --body-bg:#222222;
  --foot-bg:#1f1f1f;
  --rule:#3a3a3a;
  --soft:#d8d8d8;
  --muted:#bdbdbd;
  --serif:'Cinzel', Georgia, serif;
  --sans:'Montserrat', Arial, sans-serif;
}
*{margin:0;padding:0;box-sizing:border-box}
html,body{width:1200px;height:1099px;overflow:hidden;background:var(--body-bg)}
.page{position:relative;width:1200px;height:1099px;font-family:var(--sans)}
.site-header{position:absolute;top:0;left:0;width:1200px;height:119px;background:var(--white)}
.shop-tab{position:absolute;left:940px;top:0;width:136px;height:32px;background:var(--black);color:var(--white);font-family:var(--serif);font-size:13px;line-height:32px;text-align:center}
.brand{position:absolute;left:137px;top:56px;display:flex;align-items:center;gap:14px;font-family:var(--serif);font-size:29px;color:var(--ink);letter-spacing:.5px}
.brand-square{width:40px;height:40px;border:1.5px solid var(--ink)}
.main-nav{position:absolute;top:70px;left:483px;display:flex;font-family:var(--serif);font-size:15px;color:#333}
.main-nav span{margin-right:14px}
.main-nav span:nth-child(1){margin-right:23px}
.main-nav span:nth-child(2){margin-right:19px}
.hero{position:absolute;top:119px;left:0;width:1200px;height:442px;background:var(--black);color:var(--white);text-align:center}
.hero-photo{position:absolute;left:620px;top:0;width:490px;height:440px;background:radial-gradient(ellipse at 55% 50%,#b7bcc6 0%,#4a5578 30%,#16204a 60%,#000 85%)}
.hero-copy{position:absolute;left:130px;width:570px;top:146px}
.hero-kicker{font-size:20px;font-weight:300;letter-spacing:.5px}
.hero-title{font-size:40px;font-weight:300;letter-spacing:1px;margin-top:8px}
.hero-text{font-size:18px;font-weight:300;line-height:34px;margin-top:2px;letter-spacing:.3px}
.hero-limit{font-size:23px;font-weight:300;margin-top:12px;letter-spacing:.5px}
.dots{position:absolute;top:405px;left:552px;display:flex;gap:8px}
.dots i{width:13px;height:13px;border-radius:50%;background:var(--white)}
.dots i:first-child{background:#777}
.features{position:absolute;top:562px;left:0;width:1200px;height:196px;background:var(--band);border-bottom:2px solid #1a1a1a}
.feature{position:absolute;top:40px;width:190px;text-align:center;color:var(--white);font-size:13px;line-height:22px}
.feature svg{display:block;margin:0 auto;height:70px}
.feature .shadow{width:120px;height:14px;margin:-2px auto 10px;background:radial-gradient(ellipse,#111 0%,transparent 70%)}
.welcome{position:absolute;top:760px;left:0;width:1200px;height:250px;background:var(--body-bg);color:var(--soft)}
.welcome h1{position:absolute;left:126px;top:32px;font-size:25px;font-weight:300;color:var(--white)}
.welcome p{position:absolute;left:125px;width:949px;font-size:14px;font-weight:300;line-height:24px;text-align:justify}
.site-footer{position:absolute;top:1010px;left:0;width:1200px;height:89px;background:var(--foot-bg);border-top:1px solid var(--rule);text-align:center}
.foot-links{margin-top:16px;font-family:var(--serif);font-size:15px;color:var(--white)}
.foot-links b{font-weight:400;color:#888;margin:0 16px}
.foot-legal{margin-top:14px;font-size:12px;font-weight:300;color:var(--muted)}
.foot-legal b{font-weight:300;margin:0 8px}
</style>
</head>
<body>
<div class="page">
  <header class="site-header">
    <div class="shop-tab">SHOP VELQOR.COM</div>
    <div class="brand"><span class="brand-square"></span>VELQOR &amp; CO.</div>
    <nav class="main-nav"><span>HOME</span><span>ABOUT US</span><span>CONTACT US</span><span>COLLECTION</span><span>LIFESTYLE</span><span>MEDIA</span><span>SHOP NOW</span></nav>
  </header>

  <section class="hero">
    <div class="hero-photo" role="img" aria-label="Square steel watch with dark blue strap and diamond-set black dial"></div>
    <div class="hero-copy">
      <div class="hero-kicker">Time &amp; Space Fused Together</div>
      <div class="hero-title">The Lyra Watch Collection</div>
      <div class="hero-text">Worlds first watch with a piece of the Moon, Mars and a rare<br>space gem set underneath multiple floating diamonds</div>
      <div class="hero-limit">Entire Collection Limited to 600 Pieces</div>
    </div>
    <div class="dots"><i></i><i></i><i></i><i></i><i></i></div>
  </section>

  <section class="features">
    <div class="feature" style="left:121px">
      <svg viewBox="0 0 80 70" width="80"><path d="M6 6h30q4 0 4 4v58q-3-4-8-4H6z M74 6H44q-4 0-4 4v58q3-4 8-4h26z" fill="#e8e8e8"/><g stroke="#2e2e2e" stroke-width="2.5"><path d="M12 18h22M12 24h22M12 30h22M12 36h22M12 42h22M12 48h22M46 18h22M46 24h22M46 30h22M46 36h22M46 42h22M46 48h22"/></g></svg>
      <div class="shadow"></div>The Lyra Story</div>
    <div class="feature" style="left:312px">
      <svg viewBox="0 0 60 70" width="60"><path d="M6 2h36l14 14v52H6z" fill="#e8e8e8"/><g stroke="#2e2e2e" stroke-width="2.5"><path d="M16 24h30M16 32h30M16 40h30M16 48h30M16 56h30"/></g></svg>
      <div class="shadow"></div>Register Your Watch</div>
    <div class="feature" style="left:504px">
      <svg viewBox="0 0 60 70" width="60"><g stroke="#e8e8e8" stroke-width="7" stroke-linecap="round"><path d="M10 12l40 48M48 14L14 56"/></g><circle cx="48" cy="12" r="9" fill="#e8e8e8"/><circle cx="52" cy="8" r="4" fill="#2e2e2e"/></svg>
      <div class="shadow"></div>Repair ,Maintenance &amp;<br>Warranty Info</div>
    <div class="feature" style="left:696px">
      <svg viewBox="0 0 70 70" width="70"><path d="M4 2h36l14 14v52H4z" fill="#e8e8e8"/><g stroke="#2e2e2e" stroke-width="2.5"><path d="M12 24h30M12 32h30M12 40h30M12 48h24"/></g><circle cx="52" cy="54" r="8" fill="none" stroke="#888" stroke-width="3"/><path d="M58 60l8 8" stroke="#888" stroke-width="4"/></svg>
      <div class="shadow"></div>Register to find out about<br>New Watch collections</div>
    <div class="feature" style="left:889px">
      <svg viewBox="0 0 150 70" width="150"><g fill="#f2f2f2"><circle cx="18" cy="42" r="16"/><circle cx="55" cy="42" r="16"/><circle cx="93" cy="42" r="16"/><circle cx="131" cy="42" r="16"/></g></svg>
      <div class="shadow"></div>Spread The word</div>
  </section>

  <section class="welcome">
    <h1>Welcome to velqor &amp; co</h1>
    <p style="top:80px">When the founders of Velqor &amp; Co. had their first meeting a mantra was born: Be Amazing!</p>
    <p style="top:120px">From inception, Velqor &amp; Co. decided to create timepieces that delight the senses and impacts the wearer.&nbsp; It is for people who embrace a larger vision of themselves and the world in which they live.&nbsp; For those who embrace a sense of style, purpose and the future.The mantra, "Be Amazing" has been at the core of the company's values.&nbsp; Velqor &amp; Co. is driven to create radical yet spectacular wrist wear and timepieces; pieces that can change the jewelry landscape of today.&nbsp; Each piece is designed to inspire the wearer.</p>
  </section>

  <footer class="site-footer">
    <div class="foot-links">CONTACT US<b>|</b>TERMS OF SERVICE<b>|</b>REFUND POLICY<b>|</b>PRIVACY POLICY</div>
    <div class="foot-legal">©2013 Company Name , All Rights Reserved<b>|</b>Privacy Policy<b>|</b>Terms &amp; Conditions</div>
  </footer>
</div>
</body>
</html>
```